Employee Benefits Consulting Firm needs a refreshed website

I have a business (an employee benefits consulting firm) called Korvane Benefits Group, LLC (www.korvanebenefits-example.com).  The existing site is currently hosted on Plumhaven.  The business has been pretty much dormant since 2012.  I've relaunched the business and need a new website and looking for the website to be in Wordpress and to start with just 5 pages:
Home
About Us
Services
Contact Us
Blog
Some information about Korvane Benefits Group:
There is a tremendous waste (financial) in the traditional employee benefit model --- the current system is broken and simply stated, unsustainable. We take a very different approach when it comes to employee benefits consulting, constantly strive to provide short-term and long-term cost containment strategies that truly bend the healthcare cost curve... Many of our clients consider us as Benefit Architects...
Each employer/business is unique.
In short, our firm works with Employers to first understand their business.... -their history, their corporate structure, their leadership, their values, their uniqueness, etc.
Then we take a deep dive and get a strong grasp on their existing benefits program... -how did they get to where they are today, what are their goals/objectives, what is their risk tolerance, what are current pain points, are they compliant, etc.
Then after thorough analysis, we deliver a tailored solution. We implement the programs and manage the various aspects and moving parts of the program throughout the year.
We also are constantly analyzing the performance of the plan and monitor population health. We aggregate data and constantly refine the approach/strategy.

Updates
I made a few updates to the brief over the past couple of days...below is the updated brief:
Home
About Us
Services
Contact Us
Blog
MUST HAVE:
Mobile Friendly
PLEASE USE MERIDOX THEME
SHOULD HAVE:
the ability to add embedded video client testimonials
the ability for online chat
SHOULD NOT HAVE:
Photos from the old/existing website, I apologize for the late directive

I apologize for the delay on responding. Content is just about complete and will submit ASAP. Please let me know your availability to complete this project.

Updated content has been posted to this project.  I appreciate everybody's patience as we are working through this!

Target Market(s)
This is a BtoB website, primarily focusing on the following targets: CFOs, CEOs, Directors of Human Resources
Industry/Entity Type
Consulting
Number of Pages Required
5+ page
Requirements
Must have
- Mobile Friendly
- PLEASE USE MERIDOX THEME
Nice to have
- the ability to add embedded video client testimonials
- the ability for online chat
Should not have
- Photos from the old/existing website, I apologise for the late directive

```html
<!DOCTYPE html>
<html lang="en">
<head>
<meta charset="utf-8">
<title>Korvane Benefits Group, LLC</title>
<link rel="stylesheet" href="https://fonts.googleapis.com/css2?family=Fira+Sans:wght@300;400;500;600&display=swap">
<style>
:root{
  --green:#5aa440;
  --slate:#3d5164;
  --slate-dark:#34495c;
  --text:#4a4f55;
  --muted:#8b9096;
  --teal-light:#a6d8d1;
  --teal-mid:#7fa9a8;
  --line:#e3e5e8;
  --white:#ffffff;
}
*{box-sizing:border-box;margin:0;padding:0}
html,body{width:1200px;height:4355px;overflow:hidden;background:var(--white)}
body{font-family:"Fira Sans",sans-serif;color:var(--text);position:relative}
a{text-decoration:none}
section,header,footer{position:relative;width:1200px;overflow:hidden}
.abs{position:absolute}
.btn{position:absolute;display:flex;align-items:center;justify-content:center;border-radius:22px;font-size:13px;letter-spacing:.3px;text-transform:uppercase;text-decoration:none}
.btn-green{background:var(--green);color:var(--white)}

/* header */
.site-header{height:117px;border-bottom:1px solid var(--line)}
.brand{left:106px;top:36px;display:flex;align-items:center;gap:12px}
.brand-square{width:44px;height:44px;background:var(--green);border-radius:4px}
.brand-name{font-size:27px;font-weight:400;color:var(--slate);letter-spacing:-.3px;line-height:1}
.main-nav a{position:absolute;top:0;height:117px;display:flex;align-items:center;justify-content:center;font-size:13px;color:var(--muted);text-decoration:none;text-transform:uppercase}
.nav-home{left:517px;width:71px;background:var(--green);color:var(--white)!important}
.nav-login{left:979px;width:111px;background:var(--slate);color:var(--white)!important}
.search{left:1118px;top:48px}

/* hero */
.hero{height:618px;border-bottom:1px solid var(--line)}
.hero-photo{left:524px;top:0;width:676px;height:617px;background:linear-gradient(90deg,#ffffff 0%,#e6e7e5 12%,#cfd3d4 40%,#9ea8ae 70%,#c9ccca 100%)}
.hero h1{left:106px;top:185px;font-size:36px;font-weight:600;line-height:48px;color:var(--slate);text-transform:uppercase}
.hero p{left:108px;top:302px;width:440px;font-size:14px;line-height:26px;color:var(--slate)}
.hero .btn{left:108px;top:385px;width:179px;height:42px;text-transform:none;font-size:14px;gap:12px}

/* about */
.about{height:800px}
.about h2{left:137px;top:135px;font-size:34px;font-weight:600;color:var(--green);text-transform:uppercase}
.about-copy{left:137px;top:215px;width:548px;font-size:14px;line-height:20px;color:#3f4348;text-align:justify}
.about-copy p{margin-bottom:20px}
.about .btn-outline{left:137px;top:651px;width:167px;height:41px;border:2px solid var(--slate);color:var(--slate)}
.about-mark{left:760px;top:195px;width:400px;height:400px;border-radius:50%;background:var(--teal-light);opacity:.45}

/* programs */
.programs{height:581px;background:linear-gradient(90deg,#a5d6cf 0%,#86aba9 40%,#5f7a84 70%,#4a6073 100%)}
.programs h2{left:0;width:1200px;top:97px;text-align:center;font-size:34px;font-weight:600;color:var(--white);text-transform:uppercase}
.program{top:239px;width:300px;text-align:center;color:var(--white)}
.program-icon{width:112px;height:112px;border:2px solid var(--white);border-radius:50%;margin:0 auto;display:flex;align-items:center;justify-content:center}
.program h3{margin-top:26px;font-size:18px;font-weight:500}
.program p{margin:12px auto 0;width:262px;font-size:11.5px;line-height:20px;color:rgba(255,255,255,.85)}

/* services */
.services{height:679px}
.services h2{left:0;width:1200px;top:90px;text-align:center;font-size:34px;font-weight:600;color:var(--green);text-transform:uppercase}
.service{display:flex;align-items:center;gap:15px}
.service-icon{width:78px;height:78px;border:3px solid var(--green);border-radius:50%;display:flex;align-items:center;justify-content:center}
.service span{font-size:23px;font-weight:500;color:var(--green);text-transform:uppercase}
.services .btn{left:517px;top:547px;width:166px;height:41px}

/* cta */
.cta{height:371px;background:linear-gradient(100deg,#6f7e8c 0%,#7b8997 45%,#6d7c8b 100%)}
.cta-photo{inset:0}
.cta h2{left:0;width:1200px;top:130px;text-align:center;font-size:37px;font-weight:300;color:var(--white)}
.cta .btn{left:517px;top:228px;width:166px;height:41px}

/* blog */
.blog{height:809px}
.blog h2{left:110px;top:120px;font-size:34px;font-weight:600;color:var(--slate);text-transform:uppercase}
.blog-rule{left:110px;top:189px;width:69px;height:3px;background:var(--slate)}
.blog-intro{left:112px;top:215px;font-size:15px;line-height:32px;color:#3f4348}
.more-news{left:987px;top:246px;font-size:12px;color:var(--slate);display:flex;align-items:center;gap:10px}
.post{top:336px;width:309px}
.post-img{width:309px;height:196px}
.post h3{margin-top:46px;font-size:18px;font-weight:600;line-height:26px;color:var(--slate)}
.post p{margin-top:16px;font-size:12px;line-height:24px;color:var(--muted)}
.post time{display:block;margin-top:10px;font-size:12px;color:var(--slate)}

/* footer */
.site-footer{height:380px;background:linear-gradient(90deg,#45596d 0%,#55707f 50%,#6f9898 100%);color:var(--white)}
.footer-mark{left:750px;top:80px;width:420px;height:420px;border-radius:50%;background:rgba(255,255,255,.08)}
.footer-brand{left:108px;top:84px;display:flex;align-items:center;gap:10px}
.footer-brand .brand-square{width:34px;height:34px;background:var(--white)}
.footer-brand .brand-name{font-size:21px;color:var(--white)}
.socials{left:108px;top:168px;display:flex;gap:24px}
.socials span{width:12px;height:12px;border-radius:50%;background:var(--white)}
.copyright{left:108px;top:216px;font-size:12px}
.footer-col h4{font-size:18px;font-weight:400;margin-bottom:20px}
.quick-links{left:443px;top:90px}
.quick-links li{list-style:none;font-size:13px;line-height:30.5px}
.contact-info{left:640px;top:90px;font-size:11px;line-height:24px}
.contact-info h4{font-size:18px}
.contact-info strong{font-weight:600}
.newsletter{left:872px;top:90px}
.newsletter .field{width:232px;height:38px;border-radius:19px;background:var(--white);color:#b9bcc0;font-size:11px;padding-left:16px;display:flex;align-items:center;margin-bottom:16px}
.newsletter .submit{width:232px;height:37px;border-radius:19px;background:var(--green);font-size:12px;text-transform:uppercase;display:flex;align-items:center;justify-content:center}
</style>
</head>
<body>

<header class="site-header">
  <div class="brand abs">
    <span class="brand-square"></span>
    <div class="brand-name">Korvane Benefits Group</div>
  </div>
  <nav class="main-nav">
    <a class="nav-home" href="#">Home</a>
    <a style="left:608px;width:66px" href="#">About Us</a>
    <a style="left:706px;width:66px" href="#">Services</a>
    <a style="left:800px;width:90px" href="#">Contact Us</a>
    <a style="left:918px;width:40px" href="#">Blog</a>
    <a class="nav-login" href="#">Client Login</a>
  </nav>
  <svg class="search abs" width="18" height="18" viewBox="0 0 18 18" fill="none" stroke="#b8bcc0" stroke-width="1.6"><circle cx="7.5" cy="7.5" r="6"/><path d="M12 12l5 5"/></svg>
</header>

<section class="hero">
  <div class="hero-photo abs" role="img" aria-label="Photo of two businessmen in suits meeting at a table with laptops by a bright window"></div>
  <h1 class="abs">Control. Transparency.<br>Planning. Stability</h1>
  <p class="abs">Commitment – Our goal is long-term relationships and we realize that these are earned.</p>
  <a class="btn btn-green" href="#">
    <svg width="16" height="10" viewBox="0 0 16 10" fill="none" stroke="#fff" stroke-width="1.8"><path d="M0 5h14M10 1l4 4-4 4"/></svg>
    Learn More
  </a>
</section>

<section class="about">
  <h2 class="abs">About Us</h2>
  <div class="about-copy abs">
    <p>The key to benefits is to be competitive. At Korvane Benefits Group we know your company gains competitive advantages from an experienced and hard working team. We believe in managing people as an investment, not a cost. One of the most significant investments you make is in your people and the necessary expenses of providing better benefits than your competitors.</p>
    <p>Our ability to balance the corporate financial goal of increasing shareholder's stake in the firm with the human resources goal of providing the absolute best benefits to recruit, retain, and reward top talent has established Korvane Benefits Group as one of the leading independent employee benefits brokerage and consulting firms in the state of Texas.</p>
    <p>Our innovative team approach blends your unique needs with our creative thinking, comprehensive expertise, and in-depth resources to help you and your employees with benefit management, plan design, and employee communication.</p>
    <p>At Korvane we fully understand the correlation between benefits satisfaction and job satisfaction. A proper benefits plan has the potential to influence so many lives in hundreds of positive ways therefore we strive to help make your employees healthier and happier at work. If you have been asked, "How can we do more without spending much more?", then it is time to visit with Korvane Benefits Group.</p>
  </div>
  <a class="btn btn-outline" href="#">Learn More</a>
  <div class="about-mark abs" aria-hidden="true"></div>
</section>

<section class="programs">
  <h2 class="abs">Our Programs</h2>
  <div class="program abs" style="left:117px">
    <div class="program-icon">
      <svg width="48" height="40" viewBox="0 0 48 40" fill="#fff"><circle cx="24" cy="11" r="7"/><circle cx="10" cy="14" r="5"/><circle cx="38" cy="14" r="5"/><path d="M12 38c0-9 5-15 12-15s12 6 12 15z"/><path d="M2 36c0-7 3-12 8-12 3 0 5 1 6 3-3 3-4 6-4 9z"/><path d="M46 36c0-7-3-12-8-12-3 0-5 1-6 3 3 3 4 6 4 9z"/></svg>
    </div>
    <h3>Employee Benefits</h3>
    <p>Lorem ipsum dolor sit amet, consectetur adipisicing elit, sed do eiusmod tempor incididunt ut labore et dolore magna aliqua.</p>
  </div>
  <div class="program abs" style="left:450px">
    <div class="program-icon">
      <svg width="34" height="44" viewBox="0 0 34 44" fill="#fff"><path d="M0 0h22l12 12v32H0z"/><path d="M22 0v12h12" fill="#7a9ba0"/><rect x="7" y="20" width="20" height="3" fill="#7a9ba0"/><rect x="7" y="27" width="20" height="3" fill="#7a9ba0"/><rect x="7" y="34" width="20" height="3" fill="#7a9ba0"/></svg>
    </div>
    <h3>Property &amp; Casualty/Risk Mgmt</h3>
    <p>Lorem ipsum dolor sit amet, consectetur adipisicing elit, sed do eiusmod tempor incididunt ut labore et dolore magna aliqua.</p>
  </div>
  <div class="program abs" style="left:783px">
    <div class="program-icon">
      <svg width="44" height="44" viewBox="0 0 44 44" fill="#fff"><path d="M22 2C10 2 2 11 2 20c3-3 7-3 10 0 3-3 7-3 10 0 3-3 7-3 10 0 3-3 7-3 10 0C42 11 34 2 22 2z"/><path d="M22 19v17a4 4 0 0 1-8 0" fill="none" stroke="#fff" stroke-width="3"/></svg>
    </div>
    <h3>Life Insurance</h3>
    <p>Lorem ipsum dolor sit amet, consectetur adipisicing elit, sed do eiusmod tempor incididunt ut labore et dolore magna aliqua.</p>
  </div>
</section>

<section class="services">
  <h2 class="abs">Our Services</h2>
  <div class="service abs" style="left:172px;top:184px">
    <div class="service-icon"><svg width="36" height="36" viewBox="0 0 36 36" fill="none" stroke="#5aa440" stroke-width="1.8"><rect x="5" y="5" width="20" height="26" rx="2"/><path d="M9 12h12M9 17h8M9 22h8"/><circle cx="26" cy="22" r="6"/><path d="M23 22l2 2 4-4"/></svg></div>
    <span>Compliance with Regulations</span>
  </div>
  <div class="service abs" style="left:659px;top:184px">
    <div class="service-icon"><svg width="36" height="36" viewBox="0 0 36 36" fill="none" stroke="#5aa440" stroke-width="1.8"><rect x="6" y="8" width="24" height="18" rx="2"/><path d="M12 30h12M18 26v4"/><circle cx="18" cy="15" r="3"/><path d="M12 23c1-3 3-4 6-4s5 1 6 4"/></svg></div>
    <span>Consulting Services</span>
  </div>
  <div class="service abs" style="left:172px;top:299px">
    <div class="service-icon"><svg width="36" height="36" viewBox="0 0 36 36" fill="none" stroke="#5aa440" stroke-width="1.8"><rect x="5" y="6" width="26" height="20" rx="2"/><path d="M10 21v-4M15 21v-8M20 21v-6M25 21v-10M14 31h8M18 26v5"/></svg></div>
    <span>Plan Monitoring</span>
  </div>
  <div class="service abs" style="left:659px;top:299px">
    <div class="service-icon"><svg width="36" height="36" viewBox="0 0 36 36" fill="none" stroke="#5aa440" stroke-width="1.8"><rect x="7" y="5" width="22" height="26" rx="2"/><path d="M11 12h14M11 17h14M11 22h8"/><circle cx="24" cy="25" r="3"/></svg></div>
    <span>Claims Analysis</span>
  </div>
  <div class="service abs" style="left:172px;top:412px">
    <div class="service-icon"><svg width="36" height="36" viewBox="0 0 36 36" fill="none" stroke="#5aa440" stroke-width="1.8"><rect x="8" y="7" width="20" height="25" rx="2"/><rect x="14" y="4" width="8" height="5" rx="1"/><path d="M13 20l4 4 7-8"/></svg></div>
    <span>Dependent Audits</span>
  </div>
  <div class="service abs" style="left:659px;top:412px">
    <div class="service-icon"><svg width="36" height="36" viewBox="0 0 36 36" fill="none" stroke="#5aa440" stroke-width="1.8"><circle cx="18" cy="12" r="5"/><path d="M9 28c1-6 5-9 9-9s8 3 9 9z"/><circle cx="7" cy="9" r="2"/><circle cx="29" cy="9" r="2"/><path d="M9 10l4 1M27 10l-4 1"/></svg></div>
    <span>Custom Employee Portals</span>
  </div>
  <a class="btn btn-green" href="#">Learn More</a>
</section>

<section class="cta">
  <div class="cta-photo abs" role="img" aria-label="Photo of a smiling presenter pointing at a board while colleagues watch in a meeting room, under a slate-blue overlay"></div>
  <h2 class="abs">Innovative Thinking. Invaluable Results.</h2>
  <a class="btn btn-green" href="#">Contact Us</a>
</section>

<section class="blog">
  <h2 class="abs">Latest Blog</h2>
  <div class="blog-rule abs"></div>
  <div class="blog-intro abs">A Modern Solution for Better Benefits - Data-Driven Benefits.<br>Expertise Where and When It Matters Most.</div>
  <a class="more-news abs" href="#">
    <svg width="14" height="8" viewBox="0 0 14 8" fill="none" stroke="#3d5164" stroke-width="1.6"><path d="M0 4h12M9 1l3 3-3 3"/></svg>
    More News
  </a>
  <article class="post abs" style="left:112px">
    <div class="post-img" role="img" aria-label="Photo of a man in a navy suit and patterned tie" style="background:linear-gradient(135deg,#2a3a55 0%,#3b4c6a 50%,#8a6c58 100%)"></div>
    <h3>Providing the blueprint for high performance benefits program.</h3>
    <p>Lorem ipsum dolor sit amet, consectetur adipisicing elit, sed do eiusmod tempor...</p>
    <time>April 16, 2019</time>
  </article>
  <article class="post abs" style="left:446px">
    <div class="post-img" role="img" aria-label="Photo looking up at city skyscrapers against a blue sky with an airplane" style="background:linear-gradient(180deg,#3f6fa8 0%,#8fb3d6 45%,#4d5f6e 100%)"></div>
    <h3>Creative strategies to reduce &amp; control the cost of healthcare.</h3>
    <p>Lorem ipsum dolor sit amet, consectetur adipisicing elit, sed do eiusmod tempor...</p>
    <time>April 16, 2019</time>
  </article>
  <article class="post abs" style="left:779px">
    <div class="post-img" role="img" aria-label="Photo of hands working on a laptop and paper charts at a desk" style="background:linear-gradient(135deg,#6f8e88 0%,#c9d3cf 50%,#8fa3a6 100%)"></div>
    <h3>Your Standards are High, Our Measure is Perfection.</h3>
    <p>Lorem ipsum dolor sit amet, consectetur adipisicing elit, sed do eiusmod tempor...</p>
    <time>April 16, 2019</time>
  </article>
</section>

<footer class="site-footer">
  <div class="footer-mark abs" aria-hidden="true"></div>
  <div class="footer-brand abs">
    <span class="brand-square"></span>
    <div class="brand-name">Korvane Benefits Group</div>
  </div>
  <div class="socials abs" aria-label="Social links"><span></span><span></span><span></span><span></span></div>
  <div class="copyright abs">© 2019 Korvane Benefits Group.</div>
  <div class="footer-col quick-links abs">
    <h4>Quick Links</h4>
    <ul><li>Privacy</li><li>Story</li><li>FAQ</li><li>About</li><li>Contact</li></ul>
  </div>
  <div class="footer-col contact-info abs">
    <h4>Contact Info</h4>
    <strong>Dallas Office Location</strong><br>
    4870 Larkspur Avenue, Ste. 210<br>
    Dallas, TX 75206<br><br>
    Phone: (972) 555-0148<br>
    Email: info@korvanebenefits-example.com
  </div>
  <div class="footer-col newsletter abs">
    <h4>Subscribe Our Newsletter</h4>
    <div class="field">Full Name*</div>
    <div class="field">Email Address*</div>
    <div class="submit">Submit</div>
  </div>
</footer>

</body>
</html>
```